'Macro at Hand' flyer design.

We need a flyer design for a new company called 'Macro at hand'. We deliver high protein, frozen meals to people in their homes. Mainly aiming at the fitness community. The flyer size will be DL (210mm x 99mm).

We already have a logo as attached below, and would obviously like it to be on the flyer somewhere. We would also like the overall design of the flyer to be in line with the logo (so that the design of the flyer works with the logo and does not contrast it too much).

If you are using any visuals (pictures, background pictures etc.) please do not reference it to any food. Rather we prefer if you used fitness as your inspiration. Please see the picture of Bertil attached for guide. If you are stuck for ideas you can use this photo, however drawn in art. Any pictures you do use please ensure that you have copyright privileges to.

Be as creative as you like with the flyer design. The logo has limited colors however we do not want the flyer to look boring!

These texts will be included on the flyer in the exact order as follows:

- Live a busy lifestyle? No time to meal prep? We do it for you!

- Whether you're bodybuilding or just want truly healthy meals, order from us online.

- Grab and Go meals that you can take to work, school...anywhere.

- High protein, low fat, low sodium.

- No artificial flavours, colours or preservatives.

- Delivered straight to your door, on the day of your choice^.

- Affordable prices.

Remember, if you fail to plan then you plan to fail.

Visit us at www.macroathand.com.au

^Please visit website for conditions.

Target Market(s)

Fitness community.

Industry/Entity Type

Fitness

Requirements
Must have
• Overall design must work with logo.
Nice to have
• Colors.
Should not have
• Any pictures in reference to food.

```html
<!DOCTYPE html>
<html lang="en">
<head>
<meta charset="utf-8">
<title>Macro at Hand – Flyer</title>
<link rel="stylesheet" href="https://fonts.googleapis.com/css2?family=Montserrat:wght@400;500;600;700;800&display=swap">
<style>
  :root {
    --crimson: #a91f3c;
    --ink: #0b0b0c;
    --paper: #ffffff;
    --stage: #eeeeee;
    --text-light: #f4f4f4;
  }
  * { margin: 0; padding: 0; box-sizing: border-box; }
  html, body { width: 1200px; height: 960px; overflow: hidden; background: var(--stage); }
  body { font-family: "Montserrat", Arial, sans-serif; position: relative; }

  .flyer {
    position: absolute; left: 290px; top: 40px;
    width: 620px; height: 880px;
    background: var(--paper);
    overflow: hidden;
    box-shadow: 0 6px 24px rgba(0,0,0,.18);
  }
  .flyer__shapes { position: absolute; inset: 0; }

  .brand {
    position: absolute; left: 250px; top: 112px;
    display: flex; align-items: center; gap: 12px;
    white-space: nowrap;
  }
  .brand__mark { width: 24px; height: 24px; background: var(--crimson); flex: none; }
  .brand__name { font-size: 32px; font-weight: 800; color: var(--ink); line-height: 1; letter-spacing: -0.5px; }
  .brand__url {
    position: absolute; left: 286px; top: 168px;
    font-size: 16px; font-weight: 700; color: var(--crimson);
    white-space: nowrap;
  }

  .hook { position: absolute; left: 20px; top: 246px; color: var(--text-light); }
  .hook__question { font-size: 14px; font-weight: 600; letter-spacing: 2px; }
  .hook__headline { font-size: 38px; font-weight: 700; line-height: 1.08; margin-top: 4px; letter-spacing: -1px; }
  .hook__headline .dark { color: var(--ink); }
  .hook__answer { font-size: 13px; font-weight: 600; letter-spacing: 1.5px; margin-top: 10px; line-height: 1.3; }

  .pitch {
    position: absolute; left: 40px; top: 508px; width: 340px;
    color: var(--text-light); font-size: 12px; font-weight: 500; line-height: 1.4;
  }
  .pitch__intro { margin-bottom: 18px; }
  .pitch__list { list-style: none; }
  .pitch__list li { margin: 0 0 18px 14px; }
  .pitch__list li::before { content: "- "; }

  .motto {
    position: absolute; left: 0; width: 620px; top: 790px; text-align: center;
    color: var(--text-light); font-size: 17px; font-weight: 700;
  }
  .footnote {
    position: absolute; left: 24px; top: 830px;
    color: var(--text-light); font-size: 10px;
  }
</style>
</head>
<body>
  <main class="flyer">
    <svg class="flyer__shapes" viewBox="0 0 620 880" width="620" height="880">
      <defs>
        <radialGradient id="curlTone" cx="0.55" cy="0.45" r="0.6">
          <stop offset="0" stop-color="#6b5a50"/>
          <stop offset="0.5" stop-color="#2a2422"/>
          <stop offset="1" stop-color="#0b0b0c"/>
        </radialGradient>
        <radialGradient id="armTone" cx="0.5" cy="0.4" r="0.55">
          <stop offset="0" stop-color="#9a9a9a"/>
          <stop offset="0.45" stop-color="#3a3a3a"/>
          <stop offset="1" stop-color="#0b0b0c" stop-opacity="0"/>
        </radialGradient>
      </defs>

      <polygon class="field-dark" points="360,410 620,300 620,880 0,880 0,460" fill="var(--ink)"/>

      <polygon role="img" aria-label="Photo of an athlete curling a dumbbell" points="372,420 620,318 620,840" fill="url(#curlTone)"/>

      <ellipse role="img" aria-label="Black and white photo of a muscular arm lifting a weight with smoke" cx="490" cy="720" rx="140" ry="165" fill="url(#armTone)"/>

      <polygon class="triangle-edge" points="170,0 192,0 372,408 360,410" fill="var(--ink)"/>
      <polygon class="triangle-red" points="0,0 170,0 360,410 0,460" fill="var(--crimson)"/>

      <polygon class="band" points="0,462 360,412 620,302 620,318 366,426 0,478" fill="var(--crimson)"/>
      <polygon class="band" points="352,418 372,410 620,830 620,866" fill="var(--crimson)"/>
    </svg>

    <div class="brand">
      <span class="brand__mark"></span>
      <span class="brand__name">MACRO AT HAND</span>
    </div>
    <p class="brand__url">www.macroathand.com.au</p>

    <section class="hook">
      <p class="hook__question">Live a busy lifestyle?</p>
      <h1 class="hook__headline"><span class="dark">No time</span> to<br>meal prep?</h1>
      <p class="hook__answer">We've got your<br>macro at hand!</p>
    </section>

    <section class="pitch">
      <p class="pitch__intro">Whether you're bodybuilding or just want truly healthy meals, order from us online.</p>
      <ul class="pitch__list">
        <li>Grab and Go meals that you can take to work, school...anywhere.</li>
        <li>High protein, low fat, low sodium.</li>
        <li>No artificial flavours, colours or preservatives.</li>
        <li>Free Delivery, on the day of your choice^</li>
        <li>Affordable prices.</li>
      </ul>
    </section>

    <p class="motto">If you fail to plan then you plan to fail.</p>
    <p class="footnote">^visit website for conditions</p>
  </main>
</body>
</html>
```